Boilerplate Management Organization Chart

"Our Management Approach is a deliberate step-by-step process and supports our Technical Approach detailed in proposal submission. The Management Approach covers all the human capital aspects for executing a contract—from contract award through to sustainment and/or transition of the contract to another company. It includes how we organize, hire, staff, train, and account for our contract employees—as well as their complete personal life-cycle management within the company."

We need this management approach to depict an amazing management process that demonstrates best practices of the project management body of knowledge. We need this vector image to be applicable to any proposal without making references to any other proposals. Generic names but using strong business language.
Updates

Thanks for all designs submitted thus far. Some have stuck to the original type of chart. We would like to see a completely different way to show the same information. It has to be able to be recognized and deciphered very quickly by people who might not necessarily want to look at it. It must draw them in and make it incredibly easy to distinguish a management approach that looks fresh, infallible, and easily implemented.

Target Market(s)

Federal space, Government organizations looking for procedural efficiencies,

Industry/Entity Type

Management

Requirements
Must have
• Must not take up more than 1/3 to 1/2 of printable page and be clear.
Should not have
• Not too much color, but should stick to some color palette of some interest.

```html
<!DOCTYPE html>
<html lang="en">
<head>
<meta charset="utf-8">
<title>Management Approach</title>
<link rel="stylesheet" href="https://fonts.googleapis.com/css2?family=Exo+2:wght@400;500;600&display=swap">
<style>
  :root {
    --navy-mid: #33567a;
    --navy-dark: #22374f;
    --steel-light: #6087aa;
    --spine: #18222e;
    --ring: #c7d5e2;
    --ink-light: #ffffff;
    --page: #ffffff;
  }
  html, body { margin: 0; padding: 0; overflow: hidden; background: var(--page); }
  .canvas { display: block; width: 1077px; height: 1200px; }
  .shadowed { filter: drop-shadow(0 9px 6px rgba(0,0,0,0.22)); }
  .tone-mid { fill: var(--navy-mid); }
  .tone-dark { fill: var(--navy-dark); }
  .tone-light { fill: var(--steel-light); }
  .spine { fill: var(--spine); }
  .step-ring { stroke: var(--ring); stroke-width: 4; }
  .heading { font-family: "Exo 2", sans-serif; font-size: 36px; font-weight: 500; fill: var(--ink-light); text-anchor: middle; }
  .step-label { font-family: "Exo 2", sans-serif; font-size: 20px; font-weight: 500; fill: var(--ink-light); text-anchor: middle; }
  .step-number { font-family: "Exo 2", sans-serif; font-size: 30px; font-weight: 600; fill: var(--ink-light); text-anchor: middle; }
  .icon { fill: none; stroke: var(--ink-light); stroke-width: 1.6; stroke-linecap: round; stroke-linejoin: round; }
</style>
</head>
<body>
<svg class="canvas" viewBox="0 0 1000 1111" preserveAspectRatio="none" xmlns="http://www.w3.org/2000/svg">

  <!-- Title banner -->
  <g class="shadowed">
    <path class="tone-mid" d="M303 28 H697 V150 H524 L500 176 L476 150 H303 Z"/>
  </g>
  <text class="heading" x="500" y="97">Management Approach</text>

  <!-- Timeline spine -->
  <rect class="spine" x="491" y="206" width="18" height="735" rx="9"/>

  <!-- Step 1 -->
  <g class="step step-left">
    <g class="shadowed"><path class="tone-light" d="M219 210 H455 V257 L478 271 L455 285 V332 H219 Z"/></g>
    <g class="icon" transform="translate(337 256)">
      <path d="M-10 -16 L-4 -4 M10 -16 L4 -4 M-14 -16 H-6 L0 -6 L6 -16 H14"/>
      <circle cx="0" cy="5" r="10"/><circle cx="0" cy="5" r="3"/>
    </g>
    <text class="step-label" x="337" y="303">Responsibility Fixed</text>
    <circle class="tone-light step-ring" cx="500" cy="271" r="25"/>
    <text class="step-number" x="500" y="282">1</text>
  </g>

  <!-- Step 2 -->
  <g class="step step-right">
    <g class="shadowed"><path class="tone-mid" d="M545 291 V338 L522 352 L545 366 V413 H781 V291 Z"/></g>
    <g class="icon" transform="translate(663 325)">
      <path d="M-8 16 V-16 M-8 -14 H10 L6 -7 L10 0 H-8"/>
    </g>
    <text class="step-label" x="663" y="367">Management &amp;</text>
    <text class="step-label" x="663" y="392">Oversight</text>
    <circle class="tone-mid step-ring" cx="500" cy="352" r="25"/>
    <text class="step-number" x="500" y="363">2</text>
  </g>

  <!-- Step 3 -->
  <g class="step step-left">
    <g class="shadowed"><path class="tone-dark" d="M219 389 H455 V435 L478 449 L455 463 V511 H219 Z"/></g>
    <g class="icon" transform="translate(333 434)">
      <circle cx="0" cy="-6" r="6"/><path d="M-10 12 Q0 -2 10 12 Z"/>
      <circle cx="-12" cy="-3" r="4"/><path d="M-19 9 Q-12 1 -8 5"/>
      <circle cx="12" cy="-3" r="4"/><path d="M19 9 Q12 1 8 5"/>
    </g>
    <text class="step-label" x="333" y="485">Manning the Team</text>
    <circle class="tone-dark step-ring" cx="500" cy="449" r="25"/>
    <text class="step-number" x="500" y="460">3</text>
  </g>

  <!-- Step 4 -->
  <g class="step step-right">
    <g class="shadowed"><path class="tone-light" d="M545 470 V517 L522 531 L545 545 V592 H781 V470 Z"/></g>
    <g class="icon" transform="translate(665 515)">
      <rect x="-6" y="-14" width="18" height="13"/><path d="M-2 -9 H8 M-2 -5 H6"/>
      <circle cx="-12" cy="-8" r="3"/><path d="M-12 -4 V6 M-12 -2 L-6 -6"/>
      <circle cx="-4" cy="5" r="2"/><circle cx="3" cy="5" r="2"/><circle cx="10" cy="5" r="2"/>
      <path d="M-7 12 Q-4 8 -1 12 M0 12 Q3 8 6 12 M7 12 Q10 8 13 12"/>
    </g>
    <text class="step-label" x="663" y="566">Training</text>
    <circle class="tone-light step-ring" cx="500" cy="531" r="25"/>
    <text class="step-number" x="500" y="542">4</text>
  </g>

  <!-- Step 5 -->
  <g class="step step-left">
    <g class="shadowed"><path class="tone-mid" d="M219 567 H455 V613 L478 627 L455 641 V689 H219 Z"/></g>
    <g class="icon" transform="translate(337 603)">
      <circle cx="0" cy="0" r="12"/>
      <path d="M0 -17 V-12 M0 12 V17 M-17 0 H-12 M12 0 H17 M-12 -12 L-8.5 -8.5 M12 12 L8.5 8.5 M-12 12 L-8.5 8.5 M12 -12 L8.5 -8.5"/>
      <circle cx="0" cy="-3" r="3.5"/><path d="M-6 7 Q0 -1 6 7"/>
    </g>
    <text class="step-label" x="337" y="648">Professional</text>
    <text class="step-label" x="337" y="673">Development</text>
    <circle class="tone-mid step-ring" cx="500" cy="627" r="25"/>
    <text class="step-number" x="500" y="638">5</text>
  </g>

  <!-- Step 6 -->
  <g class="step step-right">
    <g class="shadowed"><path class="tone-dark" d="M545 648 V694 L522 708 L545 722 V770 H781 V648 Z"/></g>
    <g class="icon" transform="translate(666 680)">
      <path d="M0 -16 L2.5 -10 L9 -10 L4 -6 L6 0 L0 -4 L-6 0 L-4 -6 L-9 -10 L-2.5 -10 Z"/>
      <path d="M-16 6 H-11 V14 H-16 M-11 7 H0 Q4 7 4 10 H-3 M-11 13 H4 L14 7 Q16 5 13 4 L5 8"/>
    </g>
    <text class="step-label" x="663" y="728">Retention /</text>
    <text class="step-label" x="663" y="753">Quality of Life</text>
    <circle class="tone-dark step-ring" cx="500" cy="708" r="25"/>
    <text class="step-number" x="500" y="719">6</text>
  </g>

  <!-- Step 7 -->
  <g class="step step-left">
    <g class="shadowed"><path class="tone-light" d="M219 738 H455 V784 L478 798 L455 812 V860 H219 Z"/></g>
    <g class="icon" transform="translate(335 783)">
      <circle cx="0" cy="0" r="16"/><circle cx="0" cy="0" r="11"/><circle cx="0" cy="0" r="6"/><circle cx="0" cy="0" r="1.5"/>
      <path d="M0 0 L16 -16 M12 -18 L16 -16 L18 -12"/>
    </g>
    <text class="step-label" x="335" y="836">Benefits</text>
    <circle class="tone-light step-ring" cx="500" cy="798" r="25"/>
    <text class="step-number" x="500" y="809">7</text>
  </g>

  <!-- Step 8 -->
  <g class="step step-right">
    <g class="shadowed"><path class="tone-mid" d="M545 819 V866 L522 880 L545 894 V941 H781 V819 Z"/></g>
    <g class="icon" transform="translate(665 852)">
      <circle cx="0" cy="-8" r="7"/><path d="M-3 -1 V4 H3 V-1 M-2 7 H2"/>
      <path d="M0 -20 V-17 M-10 -16 L-8 -14 M10 -16 L8 -14"/>
      <path d="M-18 -6 V8 L-11 16 M-14 2 L-8 9 V16"/>
      <path d="M18 -6 V8 L11 16 M14 2 L8 9 V16"/>
    </g>
    <text class="step-label" x="663" y="895">Sustainment /</text>
    <text class="step-label" x="663" y="920">Transition</text>
    <circle class="tone-mid step-ring" cx="500" cy="880" r="25"/>
    <text class="step-number" x="500" y="891">8</text>
  </g>

  <!-- Closing banner -->
  <g class="shadowed">
    <rect class="tone-mid" x="303" y="961" width="394" height="122"/>
  </g>
  <text class="heading" x="500" y="1038">Program Evaluation</text>
</svg>
</body>
</html>
```